Design Labels and Brand Look For Mens Soap Company

We are developing a mens soap line for a natural body wash and exfoliating bar. We will be selling this with our line of mens toiletry bags that we sell under the name of Corvane Totes on Quillmart. We are looking for you to design the product brand look with brand color palette and fonts.

The title for the mens body was is "Body Wash For Men". The title for the soap bar is "Exfoliating Bar Soap For Men"

We are providing the templates for these 2 items in PDF form. The final version of the design needs to be in a layered PSD format. You also need to send us the fonts used.

This soap will be sold on Quillmart. Do a search for "men's body wash" and "mens soap bar" you will see our competition on page one. We need to stand out with colors and design differentiaon.

Target Market(s)

Men

Industry/Entity Type

Skin Care Product

Requirements
Must have
• Layered PSD file with all fonts

```html
<!DOCTYPE html>
<html lang="en">
<head>
<meta charset="utf-8">
<title>Corvane – Exfoliating Bar Soap Label</title>
<link rel="stylesheet" href="https://fonts.googleapis.com/css2?family=Alfa+Slab+One&display=swap">
<style>
  :root {
    --page-bg: #e4e4e4;
    --label-black: #0d0d0d;
    --label-white: #f4f4f4;
    --ornament-tone: #5a5a5a;
    --oval-light: #ffffff;
    --oval-dark: #7c7c7c;
  }
  html, body {
    margin: 0;
    padding: 0;
    width: 1200px;
    height: 881px;
    overflow: hidden;
    background: var(--page-bg);
  }
  .canvas {
    position: relative;
    width: 1200px;
    height: 881px;
  }
  .soap-label {
    position: absolute;
    left: 342px;
    top: 281px;
    width: 515px;
    height: 318px;
    display: block;
  }
  .label-type {
    font-family: "Alfa Slab One", "Rockwell", serif;
    fill: var(--label-white);
  }
  .brand-name {
    font-family: "Alfa Slab One", "Rockwell", serif;
    fill: var(--label-black);
  }
</style>
</head>
<body>
<main class="canvas">
  <svg class="soap-label" viewBox="0 0 426 263" xmlns="http://www.w3.org/2000/svg" aria-labelledby="label-title">
    <title id="label-title">Corvane Exfoliating Bar Soap For Men label</title>
    <defs>
      <radialGradient id="oval-fill" cx="50%" cy="45%" r="60%">
        <stop offset="0%" stop-color="var(--oval-light)"/>
        <stop offset="55%" stop-color="#e2e2e2"/>
        <stop offset="100%" stop-color="var(--oval-dark)"/>
      </radialGradient>
      <linearGradient id="ornament-fill" x1="0" y1="0" x2="0" y2="1">
        <stop offset="0%" stop-color="#666"/>
        <stop offset="50%" stop-color="#4a4a4a"/>
        <stop offset="100%" stop-color="#666"/>
      </linearGradient>
      <path id="arc-top" d="M 117 131 A 96 96 0 0 1 309 131"/>
      <path id="arc-bottom" d="M 104 131 A 109 109 0 0 0 322 131"/>
    </defs>

    <!-- label body -->
    <rect class="label-body" x="0" y="0" width="426" height="263" rx="4" fill="var(--label-black)"/>
    <rect class="outer-frame" x="7" y="7" width="412" height="249" fill="none" stroke="var(--label-white)" stroke-width="2"/>

    <!-- side panels -->
    <g class="side-panel side-panel--left">
      <rect x="12" y="12" width="43" height="239" fill="none" stroke="var(--label-white)" stroke-width="1.5"/>
      <rect x="17" y="17" width="33" height="229" fill="none" stroke="var(--label-white)" stroke-width="1"/>
      <rect x="22" y="24" width="23" height="215" fill="url(#ornament-fill)" role="img" aria-label="Vertical white scrollwork ornament"/>
    </g>
    <g class="side-panel side-panel--right">
      <rect x="371" y="12" width="43" height="239" fill="none" stroke="var(--label-white)" stroke-width="1.5"/>
      <rect x="376" y="17" width="33" height="229" fill="none" stroke="var(--label-white)" stroke-width="1"/>
      <rect x="381" y="24" width="23" height="215" fill="url(#ornament-fill)" role="img" aria-label="Vertical white scrollwork ornament"/>
    </g>

    <!-- central panel -->
    <rect class="center-frame" x="60" y="12" width="306" height="239" fill="none" stroke="var(--label-white)" stroke-width="1.5"/>
    <g class="corner-ornaments">
      <rect x="66" y="18" width="86" height="70" fill="url(#ornament-fill)" role="img" aria-label="Top left corner filigree"/>
      <rect x="274" y="18" width="86" height="70" fill="url(#ornament-fill)" role="img" aria-label="Top right corner filigree"/>
      <rect x="66" y="175" width="86" height="70" fill="url(#ornament-fill)" role="img" aria-label="Bottom left corner filigree"/>
      <rect x="274" y="175" width="86" height="70" fill="url(#ornament-fill)" role="img" aria-label="Bottom right corner filigree"/>
    </g>

    <!-- horizontal banner behind seal -->
    <rect class="seal-banner" x="64" y="104" width="298" height="54" fill="var(--label-black)" stroke="var(--label-white)" stroke-width="2"/>
    <rect x="70" y="110" width="286" height="42" fill="none" stroke="var(--label-white)" stroke-width="1"/>

    <!-- round seal -->
    <g class="seal">
      <circle cx="213" cy="131" r="118" fill="var(--label-black)"/>
      <circle cx="213" cy="131" r="115" fill="none" stroke="var(--label-white)" stroke-width="2"/>
      <circle cx="213" cy="131" r="111" fill="none" stroke="var(--label-white)" stroke-width="1"/>
      <circle cx="213" cy="131" r="84" fill="none" stroke="var(--label-white)" stroke-width="2"/>
    </g>

    <text class="label-type" font-size="17" letter-spacing="2.5">
      <textPath href="#arc-top" startOffset="50%" text-anchor="middle">EXFOLIATING</textPath>
    </text>
    <text class="label-type" font-size="14.5" letter-spacing="0.5">
      <textPath href="#arc-bottom" startOffset="50%" text-anchor="middle">BAR SOAP FOR MEN</textPath>
    </text>

    <!-- centre oval -->
    <ellipse class="name-oval" cx="213" cy="131" rx="78" ry="60" fill="url(#oval-fill)" stroke="var(--label-white)" stroke-width="3"/>
    <ellipse cx="213" cy="131" rx="72" ry="54" fill="none" stroke="var(--label-black)" stroke-width="1"/>

    <g class="stars" fill="var(--label-black)">
      <polygon points="213,75 214.2,78.4 217.8,78.4 214.9,80.5 216,84 213,81.9 210,84 211.1,80.5 208.2,78.4 211.8,78.4"/>
      <polygon points="213,179 214.2,182.4 217.8,182.4 214.9,184.5 216,188 213,185.9 210,188 211.1,184.5 208.2,182.4 211.8,182.4"/>
    </g>

    <text class="brand-name" x="213" y="141" font-size="27" text-anchor="middle">Corvane</text>
  </svg>
</main>
</body>
</html>
```